Velvet Strut

The site will showcase the different drag queens of Manchester and provide an area for photography, video, social media feeds (such as zingo and Kinloop) as well as reviews of Drag queens to give the public a place to discuss shows or individuals.

Target Market(s)

Gay men

Industry/Entity Type

Media

Font styles to use
Decorative

Colors

Designer to choose colors to be used in the design.

Requirements
Must have
• Bright, bold, showbiz, glamorous but a little tacky at the same time.

```html
<!DOCTYPE html>
<html lang="en">
<head>
<meta charset="utf-8">
<title>Velvet Strut</title>
<link href="https://fonts.googleapis.com/css2?family=Open+Sans:wght@400;600;700;800&display=swap" rel="stylesheet">
<style>
:root{
  --red:#e3141b;
  --red-dark:#b90f15;
  --ink:#1f1f1f;
  --night:#1b1b1c;
  --plum:#241a1c;
  --grey:#5a5a5a;
  --light:#e6e6e6;
  --white:#ffffff;
  --star:#f5c400;
}
*{box-sizing:border-box;margin:0;padding:0}
html,body{width:1200px;height:2799px;overflow:hidden;background:var(--white)}
body{position:relative;font-family:"Open Sans",Arial,sans-serif;color:var(--ink)}
.abs{position:absolute}
.photo{position:absolute;display:block}

/* header */
.header-band{left:0;top:0;width:1200px;height:448px;background:var(--night)}
.side-shapes{left:0;top:280px;width:1200px;height:560px}
.brand{left:181px;top:44px;font-size:38px;font-weight:800;color:var(--red);letter-spacing:.5px}
.search{left:832px;top:64px;width:191px;height:28px;background:#3a3a3a;border:1px solid #555;color:#ddd;font-size:11px;font-weight:700;padding:6px 8px}
.search svg{position:absolute;right:8px;top:6px}
.nav{left:177px;top:114px;display:flex;gap:22px;font-size:21px;font-weight:800;color:var(--white)}
.nav .active{color:var(--red)}
.login{left:896px;top:110px;width:127px;height:44px;background:var(--red);color:var(--white);font-weight:800;font-size:16px;display:flex;align-items:center;justify-content:center}
.slider{left:179px;top:155px;width:844px;height:368px;background:linear-gradient(110deg,#6b4a3a 0%,#5fa04a 30%,#3c7fb3 55%,#2c2c2c 80%,#7a6a55 100%)}
.dots{left:205px;top:486px;display:flex;gap:8px}
.dots span{width:15px;height:15px;border-radius:50%;background:#111;border:2px solid #111}
.dots span:first-child{background:var(--white)}

/* welcome */
.welcome-photo{left:181px;top:569px;width:388px;height:224px;background:linear-gradient(120deg,#2a1f25,#8a5a70 45%,#e9e9f0 55%,#3a2a30)}
.welcome-title{left:595px;top:568px;font-size:31px;font-weight:800;line-height:34px;text-transform:uppercase}
.welcome-title .red{color:var(--red)}
.welcome-text{left:597px;top:655px;width:413px;font-size:12.5px;line-height:23px;color:var(--grey)}

/* media */
.media-band{left:0;top:827px;width:1200px;height:436px;background:var(--plum)}
.media-title{font-size:31px;font-weight:800;color:var(--red);line-height:34px}
.media-sub{font-size:14px;font-weight:700;color:var(--white)}
.arrows{display:flex;gap:6px}
.video{left:181px;top:967px;width:459px;height:270px;background:linear-gradient(120deg,#7ad21a,#f3e23a 35%,#f25c9c 65%,#d5185e)}
.play{left:382px;top:1073px}
.gallery-main{left:675px;top:967px;width:329px;height:196px;background:linear-gradient(110deg,#b33e75,#f29ac5 40%,#f7e7ef 60%,#6b8f55)}
.thumbs{left:675px;top:1183px;display:flex;gap:7px}
.thumbs span{width:77px;height:58px}

/* reviews */
.rule{left:181px;width:836px;height:1px;background:#d8d8d8}
.section-title{font-size:25px;font-weight:800;line-height:27px;text-transform:uppercase}
.section-title .red{color:var(--red)}
.review{top:1405px;width:270px}
.review .pic{width:270px;height:176px}
.review p{margin-top:26px;font-size:12.5px;line-height:23px;color:var(--ink)}
.rating{margin-top:8px;display:flex;align-items:center;gap:4px;font-size:11px;padding-left:6px}
.rating b{color:var(--star);font-size:19px;letter-spacing:2px}
.reviewer{margin-top:8px;font-size:11px;font-weight:600}
.review-quote{font-size:17px}

/* discussion */
.parade{left:181px;top:1838px;width:528px;height:388px;background:linear-gradient(180deg,#4f7a3a 0%,#6e8b5a 35%,#9a9a98 60%,#5e5e60 100%)}
.panel{left:709px;top:1838px;width:308px;height:388px;background:var(--red)}
.notch{left:752px;top:1820px}
.comment{left:730px;width:280px}
.comment .avatar{position:absolute;left:0;top:0;width:76px;height:67px;background:linear-gradient(160deg,#c99f86,#6d4a3a);border:2px solid var(--white)}
.comment p{position:absolute;left:95px;top:2px;width:180px;color:var(--white);font-size:12.5px;line-height:21px}
.comment .who{position:absolute;left:0;top:80px;color:var(--white);font-size:11.5px;font-weight:700;white-space:nowrap}

/* social */
.divider{left:586px;top:2267px;width:1px;height:385px;background:#e0e0e0}
.social-icon{width:67px;height:67px;border-radius:50%;border:2px solid #2e5aa6}
.social-name{font-size:20px;font-weight:800}
.post{width:370px}
.post .mark{position:absolute;left:0;top:0;width:68px;height:56px;background:#f2f2f2;color:var(--red);font-size:11px;font-weight:800;display:flex;align-items:center;justify-content:center;text-align:center;line-height:13px}
.post p{position:absolute;left:84px;top:0;width:290px;font-size:12.5px;line-height:21px;color:var(--grey)}
.post .date{position:absolute;left:84px;top:68px;font-size:12px;color:var(--grey)}
.post .actions{position:absolute;left:84px;display:flex;gap:26px;font-size:12px;color:var(--grey)}
.post .actions span{display:flex;align-items:center;gap:5px}

/* footer */
.footer{left:0;top:2700px;width:1200px;height:99px;background:var(--night)}
.footer-links{left:183px;top:2730px;font-size:12px;font-weight:700;color:var(--white);word-spacing:4px}
.copyright{left:183px;top:2757px;font-size:12px;font-weight:700;color:var(--white)}
.footer-social{left:903px;top:2734px;display:flex;gap:4px}
.footer-social span{width:19px;height:19px;border-radius:50%}
</style>
</head>
<body>

<div class="abs header-band"></div>
<svg class="abs side-shapes" width="1200" height="560" viewBox="0 0 1200 560" aria-hidden="true">
  <polygon points="0,25 180,110 0,240" fill="#e3141b"/>
  <polygon points="0,240 180,110 40,250" fill="#b90f15"/>
  <polygon points="0,300 88,292 0,520" fill="#d9d9d9"/>
  <polygon points="0,300 88,292 40,330" fill="#c4c4c4"/>
  <polygon points="1200,100 1200,270 1055,270" fill="#e3141b"/>
  <polygon points="1200,260 1090,330 1200,560" fill="#d9d9d9"/>
  <polygon points="1200,260 1090,330 1150,320" fill="#c4c4c4"/>
</svg>

<div class="abs brand">Velvet Strut</div>
<div class="abs search">Search
  <svg width="14" height="14" viewBox="0 0 14 14" aria-hidden="true"><circle cx="5.5" cy="5.5" r="4" fill="none" stroke="#ddd" stroke-width="1.6"/><line x1="8.5" y1="8.5" x2="13" y2="13" stroke="#ddd" stroke-width="1.8"/></svg>
</div>
<nav class="abs nav">
  <span class="active">HOME</span><span>ABOUT US</span><span>EVENTS</span><span>COMPETITION</span><span>FAQ'S</span><span>CONTACT US</span>
</nav>
<div class="abs login">LOGIN</div>

<div class="photo slider" role="img" aria-label="Hero slide: two drag performers in bright wigs and sunglasses at a street parade"></div>
<div class="abs dots"><span></span><span></span><span></span><span></span></div>

<div class="photo welcome-photo" role="img" aria-label="Drag queens doing make-up in front of a ring light backstage"></div>
<h1 class="abs welcome-title"><span class="red">Welcome to</span><br>Velvet Strut</h1>
<p class="abs welcome-text">Lorem Ipsum is simply dummy text of the printing and typesetting industry. Lorem Ipsum has been the industry's standard dummy text ever since the 1500s, when an unknown printer took a galley of type and scrambled it to make a type specimen book. It has survived not only five centuries, but also the leap into electronic typesetting, remaining essentially unchanged Lorem Ipsum is simply dummy text of the printing and typesetting industry.</p>

<div class="abs media-band"></div>
<div class="abs" style="left:181px;top:875px">
  <h2 class="media-title">VIDEOS</h2>
  <p class="media-sub">Lorem Ipsum has been the industry's standard</p>
</div>
<svg class="abs" style="left:601px;top:891px" width="36" height="20" viewBox="0 0 36 20" aria-hidden="true"><polyline points="10,3 3,10 10,17" fill="none" stroke="#e3141b" stroke-width="3"/><polyline points="24,3 31,10 24,17" fill="none" stroke="#fff" stroke-width="3"/></svg>
<div class="abs" style="left:675px;top:875px">
  <h2 class="media-title">PHOTOGRAPHY</h2>
  <p class="media-sub">Lorem Ipsum has been the industry's standard</p>
</div>
<div class="photo video" role="img" aria-label="Video still: drag queen in a green curly wig and pink sunglasses"></div>
<svg class="abs play" width="72" height="72" viewBox="0 0 72 72" aria-hidden="true"><circle cx="36" cy="36" r="33" fill="rgba(0,0,0,.25)" stroke="#fff" stroke-width="4"/><polygon points="28,20 54,36 28,52" fill="#fff"/></svg>
<div class="photo gallery-main" role="img" aria-label="Gallery photo: drag queen in a huge pink feathered wig"></div>
<svg class="abs" style="left:683px;top:1053px" width="320" height="22" viewBox="0 0 320 22" aria-hidden="true"><polyline points="10,3 3,11 10,19" fill="none" stroke="#fff" stroke-width="3"/><polyline points="308,3 315,11 308,19" fill="none" stroke="#fff" stroke-width="3"/></svg>
<div class="abs thumbs">
  <span role="img" aria-label="Thumbnail of a performer in red" style="background:linear-gradient(135deg,#3a1a1a,#c23a3a)"></span>
  <span role="img" aria-label="Thumbnail of a queen in dark costume" style="background:linear-gradient(135deg,#2b2b2b,#b9a59a)"></span>
  <span role="img" aria-label="Thumbnail of a stage act" style="background:linear-gradient(135deg,#1c1c1c,#8a5a3a)"></span>
  <span role="img" aria-label="Thumbnail of a queen on pink" style="background:linear-gradient(135deg,#e43c8c,#5a1a3a)"></span>
</div>

<div class="abs rule" style="top:1306px"></div>
<h2 class="abs section-title" style="left:186px;top:1332px">Reviews of<br><span class="red">Drag Queens</span></h2>
<svg class="abs" style="left:962px;top:1335px" width="36" height="22" viewBox="0 0 36 22" aria-hidden="true"><polyline points="10,3 3,11 10,19" fill="none" stroke="#e3141b" stroke-width="3"/><polyline points="24,3 31,11 24,19" fill="none" stroke="#aaa" stroke-width="3"/></svg>
<div class="abs rule" style="top:1387px"></div>

<article class="abs review" style="left:184px">
  <div class="pic" role="img" aria-label="Drag queen in pink wig and yellow feathers" style="background:linear-gradient(135deg,#b3122a,#f06aa8 45%,#f4c21c)"></div>
  <p>Lorem Ipsum is simply dummy text of the printing and typesetting industry.</p>
  <div class="rating"><b>★★★★★</b>(Rating 5/5)</div>
  <div class="reviewer">Aaron Pell</div>
  <div class="review-quote">“Awesome Event</div>
</article>
<article class="abs review" style="left:464px">
  <div class="pic" role="img" aria-label="Performer with red hair singing under a white tent" style="background:linear-gradient(135deg,#f2f2f2,#e8d8d8 45%,#d21a2a 75%,#2a2a2a)"></div>
  <p>Lorem Ipsum is simply dummy text of the printing and typesetting industry.</p>
  <div class="rating"><b>★★★★★</b>(Rating 5/5)</div>
  <div class="reviewer">Aaron Pell</div>
  <div class="review-quote">Awesome Event</div>
</article>
<article class="abs review" style="left:745px">
  <div class="pic" role="img" aria-label="Drag queen dancing with a man at an event" style="background:linear-gradient(135deg,#8a7a4a,#c7a97a 45%,#3a2a22)"></div>
  <p>Lorem Ipsum is simply dummy text of the printing and typesetting industry.</p>
  <div class="rating"><b>★★★★★</b>(Rating 5/5)</div>
  <div class="reviewer">Aaron Pell</div>
  <div class="review-quote">Awesome Event</div>
</article>

<h2 class="abs section-title" style="left:181px;top:1760px">Discuss<br><span class="red">About the show</span></h2>
<h2 class="abs section-title" style="left:711px;top:1760px">On going<br><span class="red">Discussion</span></h2>
<div class="photo parade" role="img" aria-label="Street parade of drag performers in white, orange and pink costumes"></div>
<div class="abs panel"></div>
<svg class="abs notch" width="30" height="18" viewBox="0 0 30 18" aria-hidden="true"><polygon points="0,18 15,0 30,18" fill="#e3141b"/></svg>

<div class="abs comment" style="top:1866px">
  <div class="avatar" role="img" aria-label="Profile photo of a commenter"></div>
  <p>Lorem Ipsum is simply dummy text of the printing and typesetting industry.</p>
  <div class="who">Aaron Pell ,London</div>
</div>
<div class="abs comment" style="top:1989px">
  <div class="avatar" role="img" aria-label="Profile photo of a commenter"></div>
  <p>Lorem Ipsum is simply dummy text of the printing and typesetting industry.</p>
  <div class="who">Aaron Pell ,London</div>
</div>
<div class="abs comment" style="top:2114px">
  <div class="avatar" role="img" aria-label="Profile photo of a commenter"></div>
  <p>Lorem Ipsum is simply dummy text of the printing and typesetting industry.</p>
  <div class="who">Aaron Pell ,London</div>
</div>

<div class="abs social-icon" style="left:181px;top:2269px"></div>
<div class="abs social-name" style="left:265px;top:2289px">Kinloop</div>
<svg class="abs" style="left:527px;top:2294px" width="36" height="22" viewBox="0 0 36 22" aria-hidden="true"><polyline points="10,3 3,11 10,19" fill="none" stroke="#e3141b" stroke-width="3"/><polyline points="24,3 31,11 24,19" fill="none" stroke="#aaa" stroke-width="3"/></svg>
<div class="abs divider"></div>
<div class="abs social-icon" style="left:604px;top:2269px;border-color:#2fa3d9"></div>
<div class="abs social-name" style="left:690px;top:2289px">zingo</div>
<svg class="abs" style="left:981px;top:2294px" width="36" height="22" viewBox="0 0 36 22" aria-hidden="true"><polyline points="10,3 3,11 10,19" fill="none" stroke="#e3141b" stroke-width="3"/><polyline points="24,3 31,11 24,19" fill="none" stroke="#aaa" stroke-width="3"/></svg>

<div class="abs post" style="left:194px;top:2372px">
  <div class="mark">Velvet<br>Strut</div>
  <p>Sed ut perspiciatis unde omnis iste natus error sit voluptatem accusantium doloremque laudantium, totam rem aperiam, eaque ipsa quae</p>
  <div class="date">June 13, 2012 at 2:16am</div>
  <div class="actions" style="top:104px"><span>👍 Like</span><span>👎 Unlike</span><span>💬 Comment</span></div>
</div>
<div class="abs post" style="left:194px;top:2520px">
  <div class="mark">Velvet<br>Strut</div>
  <p>Sed ut perspiciatis unde omnis iste natus error sit voluptatem accusantium doloremque laudantium, totam rem aperiam, eaque ipsa quae</p>
  <div class="date">June 13, 2012 at 2:16am</div>
  <div class="actions" style="top:104px"><span>👍 Like</span><span>👎 Unlike</span><span>💬 Comment</span></div>
</div>
<div class="abs post" style="left:604px;top:2372px">
  <div class="mark">Velvet<br>Strut</div>
  <p>Lorem ipsum dolor sit amet, consectetur adipisicing elit, sed do eiusmod tempor incididunt ut labore et dolore magna aliqua.</p>
  <div class="actions" style="top:82px"><span>↩ Reply</span><span>⇄ Repost</span><span>★ Favourite</span></div>
</div>
<div class="abs post" style="left:604px;top:2520px">
  <div class="mark">Velvet<br>Strut</div>
  <p>Lorem ipsum dolor sit amet, consectetur adipisicing elit, sed do eiusmod tempor incididunt ut labore et dolore magna aliqua.</p>
  <div class="actions" style="top:82px"><span>↩ Reply</span><span>⇄ Repost</span><span>★ Favourite</span></div>
</div>

<footer class="abs footer"></footer>
<div class="abs footer-links">Home | About Us | Events | Competition | FAQ's | Contact Us</div>
<div class="abs copyright">© 2014 Company Name,All rights reserved</div>
<div class="abs footer-social">
  <span style="background:#dd4b39"></span><span style="background:#2a8ac8"></span><span style="background:#35b0e6"></span><span style="background:#e52d27"></span><span style="background:#3b5998"></span>
</div>

</body>
</html>
```